Website Wordpress Responsive Design and Development - Landscape Company

Site is currently under construction, but the old site needs a refresh.
Need a fully responsive wordpress website (built in Elementor or comparable theme).
Here's the way it looked prior :
https://pastpages.example/snap/20220330041341/http://brookmoorgreens.example/
Their current designer came up with a website sample and it looks terrible :
https://talkowenpics.sitebuild.example/mysite/projects
Websites the client likes for some inspiration, but needs better than these :
https://www.quarrinbeckgroundworkers.example/
http://kvatelierpx.example/
https://tullidgepartners.example/
https://www.garbettcoinc.example/

Navigation includes :
• Home
• Complete structure of website content is available in the home page, yielding main information on services.
• Visually appealing but simple to use and navigate. Subtle amount of content, but enough for search engines to be able to read up the target phrases.
• Sections on the home page include :
▪ About - Information about the company and main service focus
▪ Gallery - Imagery categorized to include lightbox style zoom.
▪ Contact - Contact details and connection information
• About
• Bannered header
• Content appropriately formatted to subject
• Gallery
• Bannered header
• Each of the albums would have their own categorized image content
• Contact
• Bannered header
• Social Media connector available on all pages (like box, feed, etc) if applicable
• Content can be updated on all pages
• Basic Optimization for SEO with title tags, meta data where applicable.
• Google Analytics and Sitemap installed. (google account will be provided)
• Google Business Listing and Search Console Accounts created

Coded - Design and coding required

1 page

• Wordpress Responsive Design

```html
<!DOCTYPE html>
<html lang="en">
<head>
<meta charset="utf-8">
<title>Brookmoor Greens — A Full Service Landscape Firm</title>
<link rel="stylesheet" href="https://fonts.googleapis.com/css2?family=Merriweather:wght@700&family=Montserrat:wght@300;400&family=Lora&display=swap">
<style>
  :root {
    --forest: #0b5b37;
    --accent: #a9b937;
    --accent-text: #c2cd3e;
    --white: #ffffff;
    --overlay: rgba(20, 28, 24, 0.38);
  }
  * { margin: 0; padding: 0; box-sizing: border-box; }
  html, body { width: 1200px; height: 694px; overflow: hidden; }
  body { font-family: "Montserrat", sans-serif; color: var(--white); position: relative; background: #2f3d2e; }

  .topbar {
    position: absolute; top: 0; left: 0; width: 1200px; height: 29px;
    background: var(--forest); font-size: 11px; z-index: 3;
  }
  .topbar .item { position: absolute; top: 0; height: 29px; display: flex; align-items: center; gap: 4px; white-space: nowrap; }
  .topbar .divider { position: absolute; top: 5px; width: 1px; height: 20px; background: rgba(255,255,255,0.8); }
  .topbar .phone { color: var(--accent-text); }
  .topbar svg { width: 9px; height: 10px; fill: currentColor; }

  .hero-photo {
    position: absolute; top: 29px; left: 0; width: 1200px; height: 625px;
    background:
      linear-gradient(var(--overlay), var(--overlay)),
      linear-gradient(180deg, #8e9fb3 0%, #b9c2c8 22%, #6f7d4e 40%, #4f6d2e 55%, #8c8c82 70%, #9a9a94 100%);
  }

  .brand {
    position: absolute; left: 162px; top: 38px; z-index: 2;
    font-family: "Merriweather", serif; font-weight: 700; font-size: 29px; letter-spacing: 0.3px;
  }
  .main-nav { position: absolute; top: 50px; left: 600px; width: 438px; display: flex; justify-content: space-between; z-index: 2; }
  .main-nav a { font-family: "Merriweather", serif; font-weight: 700; font-size: 11.5px; color: var(--white); text-decoration: none; }

  .hero-copy { position: absolute; left: 0; top: 248px; width: 1200px; text-align: center; z-index: 2; }
  .hero-kicker { font-family: "Lora", serif; font-size: 31px; letter-spacing: 10px; line-height: 1; }
  .hero-title { font-weight: 300; font-size: 74px; letter-spacing: 4px; line-height: 1; margin-top: 12px; }
  .hero-text { font-family: "Lora", serif; font-size: 13px; line-height: 22px; width: 830px; margin: 17px auto 0; }
  .hero-btn {
    display: inline-block; margin-top: 20px; width: 131px; height: 38px; line-height: 38px;
    background: var(--accent); border-radius: 3px; font-size: 13px; color: var(--white); text-decoration: none;
  }

  .slide-arrow { position: absolute; z-index: 2; }
  .slide-arrow.prev { left: 0; top: 303px; }
  .slide-arrow.next { right: 0; top: 316px; }

  .site-footer {
    position: absolute; left: 0; top: 654px; width: 1200px; height: 40px; background: var(--forest);
    font-size: 10.5px; display: flex; align-items: center;
  }
  .site-footer .legal { position: absolute; left: 167px; }
  .site-footer .social { position: absolute; left: 958px; display: flex; gap: 10px; }
  .site-footer .social span { width: 11px; height: 11px; border-radius: 50%; background: var(--white); display: block; }
</style>
</head>
<body>
  <header class="topbar">
    <div class="item" style="left:162px">
      <svg viewBox="0 0 12 16"><path d="M6 0a6 6 0 0 0-6 6c0 4.5 6 10 6 10s6-5.5 6-10a6 6 0 0 0-6-6zm0 8.5A2.5 2.5 0 1 1 6 3.5a2.5 2.5 0 0 1 0 5z"/></svg>
      PO Box 318 Alder Hollow, NY 11007
    </div>
    <span class="divider" style="left:384px"></span>
    <div class="item" style="left:407px">
      <svg viewBox="0 0 16 12" style="width:10px"><path d="M0 0h16v1.5L8 7 0 1.5z M0 3.3l8 5.4 8-5.4V12H0z"/></svg>
      Wes@BrookmoorGreens.example
    </div>
    <div class="item" style="left:722px">A FULL SERVICE LANDSCAPE FIRM</div>
    <span class="divider" style="left:929px"></span>
    <div class="item phone" style="left:947px">
      <svg viewBox="0 0 16 16"><path d="M3.5 0 6 3.5 4.5 5.5c1 2.2 3.8 5 6 6L12.5 10 16 12.5 14.5 16C7 16 0 9 0 1.5z"/></svg>
      (555) 014-2370
    </div>
  </header>

  <div class="hero-photo" role="img" aria-label="Photo of a shingled two-storey house with a gravel and cobblestone driveway, lawn and evergreen trees under a cloudy sky"></div>

  <div class="brand">Brookmoor Greens</div>
  <nav class="main-nav">
    <a href="#">HOME</a><a href="#">ABOUT US</a><a href="#">SERVICES</a><a href="#">GALLERY</a><a href="#">CONTACT US</a>
  </nav>

  <section class="hero-copy">
    <p class="hero-kicker">WELCOME TO</p>
    <h1 class="hero-title">BROOKMOOR GREENS</h1>
    <p class="hero-text">At an early age, Wes Harlow began mowing lawns for local families. As he got older, the number of lawn accounts began to grow. In 1998, Wes Harlow incorporated his small maintenance company taking it to the next level.</p>
    <a class="hero-btn" href="#">GET STARTED</a>
  </section>

  <svg class="slide-arrow prev" width="40" height="78" viewBox="0 0 40 78">
    <polygon points="0,0 40,39 0,78" fill="#a9b937"/>
    <polyline points="15,26 3,39 15,52" fill="none" stroke="#fff" stroke-width="2"/>
  </svg>
  <svg class="slide-arrow next" width="40" height="78" viewBox="0 0 40 78">
    <polygon points="40,0 0,39 40,78" fill="#a9b937"/>
    <polyline points="25,26 37,39 25,52" fill="none" stroke="#fff" stroke-width="2"/>
  </svg>

  <footer class="site-footer">
    <p class="legal">2022 copyrights © Brookmoor Greens &nbsp;|&nbsp;&nbsp;&nbsp;&nbsp; All rights reserved.</p>
    <div class="social" aria-label="Social links"><span></span><span></span><span></span><span></span></div>
  </footer>
</body>
</html>
```